Crestline Gas and Plumbing Business Card Design

I am after a business card design for my plumbing business called 'Crestline Gas & Plumbing'. I do all types of plumbing and gas work and specialise in general maintenance plumbing. Would like to see designs using current logo

Industry/Entity Type

Plumbing

Contact Information for Business Card

Name - Dale Whitcombe
Phone number - 0455163027
Email - admin@crestlinegasandplumbing.example.com.au
ABN - 68204915336

```html
<!DOCTYPE html>
<html lang="en">
<head>
<meta charset="utf-8">
<title>Crestline Gas &amp; Plumbing — Business Card</title>
<link href="https://fonts.googleapis.com/css2?family=Roboto:wght@400;700&display=swap" rel="stylesheet">
<style>
  :root {
    --bg: #e9e9e9;
    --card: #fdfdfd;
    --brand-blue: #1f5fae;
    --brand-orange: #f0960e;
    --ink: #111111;
    --rule: #f0a640;
  }
  * { box-sizing: border-box; margin: 0; padding: 0; }
  html, body {
    width: 1200px;
    height: 800px;
    overflow: hidden;
    background: var(--bg);
    font-family: "Roboto", Arial, sans-serif;
  }
  .canvas {
    position: relative;
    width: 1200px;
    height: 800px;
  }
  .card {
    position: absolute;
    top: 278px;
    width: 420px;
    height: 240px;
    background: var(--card);
  }
  .card--front { left: 141px; }
  .card--back { left: 637px; }

  /* Front: centred brand name */
  .brand {
    display: flex;
    align-items: center;
    gap: 12px;
    color: var(--brand-blue);
    font-weight: 700;
  }
  .brand__dot {
    flex: none;
    border-radius: 50%;
    background: var(--brand-blue);
  }
  .card--front .brand {
    position: absolute;
    left: 72px;
    top: 88px;
  }
  .card--front .brand__dot { width: 54px; height: 54px; }
  .card--front .brand__name {
    display: flex;
    flex-direction: column;
    line-height: 1;
  }
  .card--front .brand__main {
    font-size: 34px;
    letter-spacing: 1px;
    text-transform: uppercase;
  }
  .card--front .brand__sub {
    font-size: 12.5px;
    letter-spacing: 2px;
    text-transform: uppercase;
    margin-top: 5px;
  }

  /* Back */
  .holder-name {
    position: absolute;
    left: 43px;
    top: 56px;
    font-size: 20px;
    font-weight: 700;
    color: var(--brand-orange);
  }
  .card--back .brand {
    position: absolute;
    right: 45px;
    top: 54px;
    gap: 6px;
  }
  .card--back .brand__dot { width: 26px; height: 26px; }
  .card--back .brand__name {
    display: flex;
    flex-direction: column;
    line-height: 1;
  }
  .card--back .brand__main {
    font-size: 17px;
    text-transform: uppercase;
  }
  .card--back .brand__sub {
    font-size: 6.5px;
    letter-spacing: 0.8px;
    text-transform: uppercase;
    margin-top: 2px;
  }
  .divider {
    position: absolute;
    left: 43px;
    top: 113px;
    width: 332px;
    height: 1px;
    background: var(--rule);
  }
  .contact {
    position: absolute;
    left: 43px;
    top: 132px;
    list-style: none;
    color: var(--ink);
    font-size: 14.5px;
  }
  .contact__item {
    display: flex;
    align-items: center;
    gap: 6px;
    height: 21px;
  }
  .contact__icon { width: 15px; height: 15px; flex: none; }
  .contact__item--email { font-size: 13.6px; }
  .abn {
    position: absolute;
    right: 45px;
    top: 180px;
    font-size: 12.5px;
    color: var(--ink);
  }
</style>
</head>
<body>
<main class="canvas">

  <section class="card card--front" aria-label="Card front">
    <div class="brand">
      <span class="brand__dot"></span>
      <span class="brand__name">
        <span class="brand__main">Crestline</span>
        <span class="brand__sub">Gas &amp; Plumbing</span>
      </span>
    </div>
  </section>

  <section class="card card--back" aria-label="Card back">
    <h1 class="holder-name">Dale Whitcombe</h1>
    <div class="brand">
      <span class="brand__dot"></span>
      <span class="brand__name">
        <span class="brand__main">Crestline</span>
        <span class="brand__sub">Gas &amp; Plumbing</span>
      </span>
    </div>
    <div class="divider"></div>
    <ul class="contact">
      <li class="contact__item contact__item--phone">
        <svg class="contact__icon" viewBox="0 0 16 16" aria-hidden="true">
          <rect x="1" y="3" width="14" height="10" rx="1" fill="var(--brand-orange)"/>
          <path d="M1.5 3.8 L8 9 L14.5 3.8" fill="none" stroke="#fff" stroke-width="1.3"/>
        </svg>
        <span>0455163027</span>
      </li>
      <li class="contact__item contact__item--email">
        <svg class="contact__icon" viewBox="0 0 16 16" aria-hidden="true">
          <circle cx="8" cy="8" r="7.5" fill="var(--brand-orange)"/>
          <path d="M5.3 4.3 L6.8 4 L7.6 6.1 L6.7 6.9 C7.2 8.1 7.9 8.8 9.1 9.3 L9.9 8.4 L12 9.2 L11.7 10.7 C8.2 11.2 4.8 7.8 5.3 4.3 Z" fill="#fff"/>
        </svg>
        <span>admin@crestlinegasandplumbing.example.com.au</span>
      </li>
    </ul>
    <p class="abn">ABN - 68204915336</p>
  </section>

</main>
</body>
</html>
```